Creative Homepage Design

This is for a security system specifically targeted to:

BANK OWNED PROPERTIES
VACATION HOMES
COMMERCIAL PROPERTIES

The main slides will click into these sections of the website.

The 3 boxes below will link to other sections but should be focused around those topics.

Target Market(s)

BANK OWNED PROPERTIES
VACATION HOMES
COMMERCIAL PROPERTIES

Industry/Entity Type

Security

Requirements
Must have
• must use logo attached
must be designed to the sitemap
must use images that can be purchased from an image database. You will need to provide the detail of where to find the images so that we can purchase.
Nice to have
• Like these designs:
http://www.quorvantelabs.com/
http://www.belmarrowhealth.com/

```html
<!DOCTYPE html>
<html lang="en">
<head>
<meta charset="utf-8">
<title>VANTORRA – Property Security</title>
<link href="https://fonts.googleapis.com/css2?family=Arimo:wght@400;700&family=Tinos:wght@700&display=swap" rel="stylesheet">
<style>
:root{
  --red:#e3121b;
  --red-dark:#c50a12;
  --text:#2b2b2b;
  --muted:#555;
  --page:#ffffff;
  --topbar-top:#ffffff;
  --topbar-bottom:#e6e6e6;
  --panel:#f3f3f3;
  --panel-edge:#d4d4d4;
  --button:#333;
  --footer:#6d6c71;
  --footer-text:#f2f2f2;
  --icon:#a9a8ad;
}
*{margin:0;padding:0;box-sizing:border-box}
html,body{width:1200px;height:1054px;overflow:hidden}
body{position:relative;background:var(--page);font-family:"Arimo",Arial,sans-serif;color:var(--text)}
.topbar{position:absolute;left:0;top:0;width:1200px;height:49px;background:linear-gradient(var(--topbar-top),var(--topbar-bottom));border-bottom:1px solid #d0d0d0}
.util-nav{position:absolute;right:30px;top:17px;font-size:15px;color:#333}
.util-nav a{color:#333;text-decoration:none}
.util-nav .sep{margin:0 8px}
.masthead{position:absolute;left:0;top:49px;width:1200px;height:107px;background:linear-gradient(#fff,#f4f4f4)}
.brand{position:absolute;left:26px;top:28px;font-family:"Tinos",serif;font-weight:700;font-size:46px;color:var(--red);letter-spacing:1px}
.main-nav{position:absolute;left:298px;top:34px;display:flex;align-items:center;font-size:16px}
.main-nav a{color:#333;text-decoration:none;margin-right:29px}
.main-nav a.active{background:linear-gradient(#ff5a5f,var(--red) 55%,var(--red-dark));color:#333;padding:11px 14px;border:1px solid #b5060c;width:212px;margin-right:14px}
.hero{position:absolute;left:28px;top:156px;width:1148px;height:411px;background:linear-gradient(110deg,#5d83b5 0%,#8aa7c9 22%,#3d3f42 30%,#7c8f83 55%,#a8b9c4 78%,#4a4d51 100%)}
.features{position:absolute;left:28px;top:594px;width:1148px;height:300px;display:flex;border:1px solid var(--panel-edge);box-shadow:0 2px 3px rgba(0,0,0,.12)}
.feature{position:relative;flex:1;background:linear-gradient(90deg,#f7f7f7,#eaeaea 80%,#dcdcdc);border-right:1px solid var(--panel-edge)}
.feature:last-child{border-right:none}
.feature h2{position:absolute;left:34px;top:28px;font-size:25px;font-weight:700;color:var(--red);letter-spacing:.5px}
.feature p{position:absolute;left:27px;top:79px;font-size:15px;line-height:23.5px;color:var(--text);width:310px}
.feature .art{position:absolute;display:block}
.feature .more{position:absolute;bottom:14px;width:96px;height:28px;background:var(--button);color:#eee;font-size:14px;text-align:center;line-height:28px;text-decoration:none}
.footer{position:absolute;left:0;top:928px;width:1200px;height:126px;background:var(--footer);color:var(--footer-text);font-size:11.5px}
.footer .legal{position:absolute;left:47px;top:49px;line-height:17px;letter-spacing:.4px}
.socials{position:absolute;left:1014px;top:48px;display:flex;gap:14px}
.socials span{width:25px;height:25px;border-radius:50%;background:var(--icon)}
</style>
</head>
<body>
<header class="topbar">
  <nav class="util-nav"><a href="#">Home</a><span class="sep">|</span><a href="#">About us</a><span class="sep">|</span><a href="#">Customer Login</a></nav>
</header>
<div class="masthead">
  <div class="brand">VANTORRA</div>
  <nav class="main-nav">
    <a class="active" href="#">Bank Owned Prvoperties</a>
    <a href="#">Vacation Homes</a>
    <a href="#">Commercial Properties</a>
    <a href="#">How it Works</a>
    <a href="#">Support</a>
    <a href="#">Contact Us</a>
  </nav>
</div>
<section class="hero" role="img" aria-label="Security operator on the phone pointing at a wall of surveillance monitors showing an industrial site with an alarm"></section>
<section class="features">
  <article class="feature">
    <h2>Piece Of Mind</h2>
    <p>Avoid vandalism &amp; unauthorised entries<br>Documentation of all enteries<br>Reduce claim exposure of unsecured properties</p>
    <div class="art" role="img" aria-label="Padlock resting on banknotes" style="left:88px;top:158px;width:258px;height:138px;background:radial-gradient(ellipse at 60% 60%,#3a3a3a 0 18%,#d9cfb8 30%,rgba(235,235,235,0) 70%)"></div>
    <a class="more" href="#" style="left:260px">view more</a>
  </article>
  <article class="feature">
    <h2>Security From $ Price</h2>
    <p>Always Customized Notifications<br>Stay Connected from anywhere</p>
    <div class="art" role="img" aria-label="Red dollar sign on a target surrounded by question marks" style="left:145px;top:124px;width:222px;height:160px;background:radial-gradient(ellipse at 50% 60%,#d8151d 0 22%,#ffffff 30%,#cfcfcf 45%,rgba(235,235,235,0) 70%)"></div>
    <a class="more" href="#" style="left:264px">view more</a>
  </article>
  <article class="feature">
    <h2>Get Started</h2>
    <p>Demo the Web house watch<br>system info</p>
    <div class="art" role="img" aria-label="Red house connected to a computer mouse" style="left:166px;top:136px;width:190px;height:152px;background:radial-gradient(ellipse at 55% 45%,#d8151d 0 25%,#f5f5f5 45%,rgba(235,235,235,0) 70%)"></div>
    <a class="more" href="#" style="left:259px">view more</a>
  </article>
</section>
<footer class="footer">
  <div class="legal">Privacy Policy<br>© 2012 VANTORRA, All Rights Reserved</div>
  <div class="socials" aria-label="Social links"><span></span><span></span><span></span><span></span></div>
</footer>
</body>
</html>
```